Maple Harbour Website

We are starting a marketing company and to do that we need a website! We want a website that will inspire and persuade to bring out the awesomeness in our clients.
What we want to see:
- Inspirational and persuasive imagery that relate to Branding.
- No cliche images eg. business man, suits and hand shakes
- We want to transform and educate our clients.
- We want to show them the path and would like our website to really act as a guide that guides them step by step through our process.
- We want the portray that we are an investment but not have a pretentious way to it. We put our heart into every project and that is how we treat our clients.
-When you submit your design please include what platform you have created for. Preference would be Wordpress or Joobla.

We have included the psd file for the wire frame, logo files, font files, site map and a link to a video we create to give you more information on what we would like to see. http://clipvault-example.com/t/qk82LmPzr

Feel free to make small modification to the logos if you think it will improve it. Your creativity and advice is most welcome.
Updates

One thing we forgot. We would like to have our contact information near the top of the website as well as at the bottom.  Here is out contact info:

Email: info@mapleharbour.ca
Phone: 403-555-0142

Reason: As we are new with the platform and that we want to optimize our results, we decided to extend the deadline by 15 days. Thanks!

Target Market(s)

28-60, Male and Female, Oil field, Local Businesses, Dentists, Chiropractors, Hair salon, Construction/Renovation, Events etc

Industry/Entity Type

Investment

Requirements
Must have
• - 4 Inspirational and persuasive Imagery for the top portion of the website
- Must have a feel as if your not on a website an example of this is linked below.
http://www.pixelforum-sample.com/design/472093/web-design-by-helen-dawes
Nice to have
• - Creative advice from you.
- Creative buttons for Get Free Quote and Subscribe buttons. Something out of the box that draws peoples attention. eg. a 'B' button. Just and example but still something related to branding.
Should not have
• No Cliches

```html
<!DOCTYPE html>
<html lang="en">
<head>
<meta charset="utf-8">
<title>Maple Harbour</title>
<link href="https://fonts.googleapis.com/css2?family=Open+Sans:wght@400;600;700&family=Arimo:wght@400;700&display=swap" rel="stylesheet">
<style>
:root{
  --grey-top:#b8b9bf;
  --sidebar:#dedee2;
  --text:#888a8c;
  --text-dark:#666768;
  --text-light:#aaabad;
  --green:#8dc21f;
  --green-bright:#a0d400;
  --green-dark:#6fa80a;
  --link:#1a8fdc;
  --panel:#f6f6f8;
  --footer:#eaeaea;
  --fb:#3b5998;
  --tw:#1e9bd7;
}
*{margin:0;padding:0;box-sizing:border-box}
html,body{width:1200px;height:1000px;overflow:hidden}
body{position:relative;background:linear-gradient(180deg,var(--grey-top) 0,#d6d7db 160px,#fff 380px,#fff 100%);font-family:"Open Sans",sans-serif;color:var(--text)}
.sidebar{position:absolute;left:92px;top:0;width:240px;height:320px;background:linear-gradient(180deg,var(--sidebar) 0,rgba(238,238,240,.8) 200px,rgba(255,255,255,0) 100%)}
.brand{position:absolute;left:155px;top:62px;display:flex;align-items:center;gap:7px;font-size:13px;font-weight:600;letter-spacing:.5px;color:var(--text)}
.brand-mark{width:10px;height:10px;background:var(--green)}
.main-nav{position:absolute;left:153px;top:141px;list-style:none}
.main-nav li{font-size:15px;line-height:24px;color:var(--text-light);text-transform:uppercase}
.main-nav li.active{color:var(--green)}
.steps{position:absolute;left:382px;top:50px;display:flex;gap:14px}
.step{width:163px}
.step h2{font-family:"Arimo",sans-serif;font-weight:400;font-size:17px;color:#8a8b8e;text-shadow:0 1px 0 #f3f3f3;height:26px;line-height:24px}
.step .photo{height:96px;box-shadow:0 10px 8px -6px rgba(0,0,0,.55)}
.intro{position:absolute;left:381px;top:203px;width:700px;font-family:"Arimo",sans-serif;font-size:12px;line-height:24px;color:#777}
.social{position:absolute;left:154px;top:326px;display:flex;gap:6px}
.social span{width:29px;height:29px;display:block}
.social .fb{background:var(--fb)}
.social .tw{background:var(--tw)}
.newsletter{position:absolute;left:380px;top:325px;font-size:22px;letter-spacing:-.3px;color:var(--text)}
.newsletter strong{font-weight:600}
.btn{position:absolute;color:#fff;font-weight:700;font-size:14px;text-align:center;line-height:29px;height:29px}
.btn-subscribe{left:878px;top:326px;width:100px;background:linear-gradient(180deg,var(--green-bright),var(--green-dark))}
.welcome{position:absolute;left:257px;top:407px;width:660px;height:388px;background:var(--panel);padding:42px 59px}
.welcome h1{font-size:24px;font-weight:700;color:var(--text);margin-bottom:4px}
.welcome p{font-size:18px;line-height:21.5px;margin-bottom:22px;letter-spacing:-.1px}
.welcome .more{font-size:16px;line-height:20px;width:400px;margin-top:20px;letter-spacing:-.2px}
.welcome .more a{color:var(--link);text-decoration:none}
.btn-quote{left:484px;top:290px;width:128px;background:var(--green-bright)}
.site-footer{position:absolute;left:0;top:879px;width:1200px;height:61px;background:var(--footer)}
.footer-nav{position:absolute;left:91px;top:10px;font-family:"Arimo",sans-serif;font-weight:700;font-size:14px;color:var(--text-dark)}
.footer-nav .sep{color:#bbb;font-weight:400;margin:0 8px}
.copyright{position:absolute;left:91px;top:36px;font-size:12px;color:#bbbcbe}
.contact{position:absolute;right:124px;top:8px;text-align:right;font-size:15px;line-height:23px;color:var(--text-dark)}
.contact b{font-weight:700}
</style>
</head>
<body>
<aside class="sidebar"></aside>
<div class="brand"><span class="brand-mark"></span>MAPLE HARBOUR</div>
<ul class="main-nav">
  <li class="active">Strategy</li>
  <li>Portfolio</li>
  <li>About Us</li>
  <li>Contact Us</li>
  <li>Blog</li>
</ul>

<section class="steps">
  <div class="step"><h2>Maple Harbour</h2><div class="photo" role="img" aria-label="Branding iron glowing in a fire" style="background:linear-gradient(135deg,#4a3a2e,#c0562a 45%,#6b5a4a)"></div></div>
  <div class="step"><h2>Be Found</h2><div class="photo" role="img" aria-label="Child peeking out from under a bed" style="background:linear-gradient(180deg,#3a3a3a 0,#9aa8b4 30%,#c7c9cc 70%,#b06a5a)"></div></div>
  <div class="step"><h2>Connect</h2><div class="photo" role="img" aria-label="Hand touching a network of connected people icons" style="background:linear-gradient(180deg,#7fb0d2,#c9dbe8 60%,#e8eef2)"></div></div>
  <div class="step"><h2>Get Growing</h2><div class="photo" role="img" aria-label="Young green sprout growing from soil" style="background:linear-gradient(180deg,#c8e06a,#8cc23a 60%,#4a3a22)"></div></div>
</section>

<p class="intro">Lorem ipsum dolor sit amet, consectetur adipisicing elit, sed do eiusmod tempor incididunt ut labore et dolore magna aliqua. Ut enim ad minim veniam, quis nostrud exercitation ullamco laboris nisi ut aliquip ex ea commodo consequat.</p>

<div class="social"><span class="fb"></span><span class="tw"></span></div>
<div class="newsletter">Get Tips and Tricks! <strong>Subscribe</strong> to our Newsletter.</div>
<div class="btn btn-subscribe">Subscribe</div>

<section class="welcome">
  <h1>WELCOME!</h1>
  <p>This is just a bunch of words put toghether to make it look like paragraph. It is purly for show and filler so that we can have a general idea of what it will ook like when we put in the proper pagaraphs that make up our mission statment.</p>
  <p>I think this font size looks pretty good but maybe be a tad bit smaler. I would liketo see the welcome a little more dramatic looking. I think that is all I need to write here for now.</p>
  <p class="more">If you would like to have more information on howwe can help you achive your goals, you can visit our <a href="#">strategy</a> page or simply get a <a href="#">free quote</a>!</p>
  <div class="btn btn-quote">Get a Free Quote!</div>
</section>

<footer class="site-footer">
  <nav class="footer-nav">Site Map<span class="sep">|</span>Strategy<span class="sep">|</span>Portfolio<span class="sep">|</span>About Us<span class="sep">|</span>Contact Us<span class="sep">|</span>Blog</nav>
  <div class="copyright">©MAPLE HARBOUR INC. 2013</div>
  <div class="contact"><b>Email:</b> info@mapleharbour.ca<br><b>Phone:</b> 403-555-0142</div>
</footer>
</body>
</html>
```